Wellness Coach/Personal trainer needs wordpress site/blog with ecommerce capable membership area

We need a WordPress design for PlumHarborFit.com. This is a blog about wellness, weight loss, and health related topics. Design logo will be provided to the winner.

A great site with a design that we would like to emulate are http://kq4.example. The design should be simple, clean, unique, fun, and distinctive. Above all, it should be highly readable and easy to navigate.

These are the specific sections/categories of the blog that should be included and incorporated into the design SEE BELOW.

Thanks in advance for your consideration
Updates

Reason: I have extended the deadline to evaluate more designs from other pros

Hello all, Please take a minute to review the requirements for this project and please make sure you are capable of meeting ALL the requirements. As you already know I will be making a decision very shortly on whose design I will be moving forward with, if there are any last minute submissions now is the time. Thank you for your time.

Target Market(s)

90 % women 10 % men my clients are usually professionals who value their appearance, health, longevity and time.

Industry/Entity Type

Personal Trainer

Font styles to use
Serif

Colors
886aae
ffcf3e

Requirements
Must have
• Requirements

- start losing weight today.... 555 902 6148 (first line)
- visuals/images and backgrounds to give the idea of wellness, weight loss, healthy living, etc
- navigation menu - home, who we are, what we do, who we serve, blog, contact, members area

1) slider element at top below navigation menu
2) slider element near bottom of page will have testimonials
3) contact form/inquiry form (one page)
4) will provide wellness logo (to give credibility)
5) color scheme purple, gold and white
6) membership area
7) fb, tw, youtube icons
8) footer area - In the footer, there will be smaller company logo, copyright,
disclaimer, privacy policy, terms n conditions, verse of day, and contact info, Phone: (555) 902-6148
Email: support@...
Address:
9) use dummy content/graphic as they will be replaced by real content (the winner will provide instruction on how to make changes to all text and changing graphics)
9) ecommerce enabled / newsletter signup area

```html
<!DOCTYPE html>
<html lang="en">
<head>
<meta charset="utf-8">
<title>PlumHarborFit — Wellness &amp; Personal Training</title>
<link href="https://fonts.googleapis.com/css2?family=Open+Sans:ital,wght@0,400;0,600;0,700;0,800;1,400&display=swap" rel="stylesheet">
<style>
:root{
  --purple:#5f2472;
  --purple-dark:#4a1a5a;
  --gold:#f6c633;
  --gold-deep:#f0b81e;
  --ink:#333333;
  --muted:#7a7a7a;
  --light:#efefef;
  --line:#dddddd;
  --footer:#2c2c2c;
  --footer-bottom:#1e1e1e;
  --white:#ffffff;
}
*{box-sizing:border-box;margin:0;padding:0}
html,body{width:1200px;height:2548px;overflow:hidden;background:var(--white)}
body{font-family:"Open Sans",Arial,sans-serif;color:var(--ink);position:relative}
.wrap{position:absolute;left:80px;width:1040px}
a{color:inherit;text-decoration:none}

/* header */
.site-header{position:absolute;top:0;left:0;width:1200px;height:88px;background:var(--white)}
.brand{position:absolute;left:80px;top:26px;font-size:30px;font-weight:800;color:var(--purple);display:flex;align-items:center;gap:10px}
.brand-dot{width:18px;height:18px;border-radius:50%;background:var(--gold)}
.tagline{position:absolute;left:360px;top:10px;font-size:10px;color:var(--muted);letter-spacing:.3px}
.utility{position:absolute;right:80px;top:10px;font-size:10px;color:var(--muted);display:flex;gap:14px;font-weight:600}
.main-nav{position:absolute;right:80px;top:44px;display:flex;align-items:center;gap:2px}
.main-nav a{font-size:11px;font-weight:700;color:var(--ink);padding:9px 11px;text-transform:uppercase}
.main-nav a.current{background:var(--purple);color:var(--white)}
.main-nav .search{margin-left:8px;width:16px;height:16px}

/* hero */
.hero{position:absolute;top:88px;left:0;width:1200px;height:360px;overflow:hidden}
.hero-art{position:absolute;inset:0;background:linear-gradient(100deg,#d7ebf5 0%,#e8f4f9 45%,#cfe4ef 100%)}
.hero-figure{position:absolute;left:560px;top:10px;width:300px;height:350px;background:radial-gradient(ellipse at 50% 45%,#9ad27a 0%,#f2c9a6 35%,rgba(232,244,249,0) 70%)}
.hero-title{position:absolute;left:80px;top:168px;background:var(--white);padding:8px 16px;font-size:30px;font-weight:800;line-height:1.1;color:var(--ink);text-transform:uppercase;width:320px}
.hero-sub{position:absolute;left:80px;top:252px;background:#3a3a3a;color:var(--white);padding:10px 16px;font-size:28px;font-weight:800;text-transform:uppercase;width:440px}
.hero-note{position:absolute;left:80px;top:308px;background:var(--purple);color:var(--white);padding:5px 16px;font-size:11px;font-weight:700;text-transform:uppercase}
.arrow{position:absolute;width:34px;height:34px}
.hero .arrow.prev{left:18px;top:162px}
.hero .arrow.next{right:18px;top:162px}

/* member band */
.member-band{position:absolute;top:468px;left:0;width:1200px;height:60px;background:var(--purple)}
.member-band p{position:absolute;left:80px;top:18px;color:var(--white);font-size:17px;font-weight:600}
.btn-gold{position:absolute;right:80px;top:15px;background:var(--gold);color:var(--purple-dark);font-size:11px;font-weight:800;padding:8px 20px;text-transform:uppercase}

/* features */
.features{top:560px;display:grid;grid-template-columns:repeat(3,1fr);gap:30px}
.feature-photo{position:relative;height:184px}
.photo-workout{background:linear-gradient(135deg,#8b8f96,#c9c2b8)}
.photo-living{background:linear-gradient(135deg,#b9c9cf,#e2d6c9)}
.photo-loss{background:linear-gradient(135deg,#c7b3a3,#6f5a4d)}
.tag{position:absolute;left:0;bottom:10px;background:var(--purple);color:var(--white);font-size:10px;font-weight:700;padding:4px 10px}
.feature h3{margin-top:22px;font-size:16px;font-weight:800;color:var(--purple);text-transform:uppercase}
.feature p{margin-top:8px;font-size:11px;line-height:1.6;color:var(--muted)}

/* benefits */
.benefits-band{position:absolute;top:904px;left:0;width:1200px;height:216px;background:var(--light)}
.benefits{top:926px;display:grid;grid-template-columns:repeat(3,1fr);gap:30px}
.benefit-head{display:flex;align-items:center;gap:14px}
.benefit-icon{width:50px;height:50px;border-radius:50%;background:#4a4a4a;display:flex;align-items:center;justify-content:center}
.benefit-head h4{font-size:12px;font-weight:800;color:var(--purple);text-transform:uppercase}
.benefit ul{margin-top:12px;list-style:none}
.benefit li{font-size:11px;color:var(--muted);line-height:1.9;padding-left:14px;position:relative}
.benefit li::before{content:"";position:absolute;left:0;top:8px;width:5px;height:5px;border-radius:50%;background:var(--purple)}

/* call out */
.callout{top:1150px;height:130px}
.callout p{width:880px;font-size:20px;font-weight:800;color:var(--purple);line-height:1.35;text-transform:uppercase;margin-top:12px}
.more-circle{position:absolute;right:0;top:0;width:110px;height:110px;border-radius:50%;background:var(--purple);color:var(--white);font-size:13px;font-weight:800;display:flex;align-items:center;justify-content:center;text-align:center;line-height:1.2}
.pill{position:absolute;right:6px;top:118px;background:#3a3a3a;color:var(--white);font-size:8px;font-weight:700;padding:3px 10px;border-radius:10px}

/* latest */
.section-title{display:flex;align-items:center;gap:14px;font-size:16px;font-weight:800;color:var(--purple);text-transform:uppercase}
.section-title::after{content:"";flex:1;height:1px;background:var(--line)}
.latest{top:1300px}
.post-grid{margin-top:28px;display:flex;gap:12px}
.post-thumb{width:165px;height:128px}
.t1{background:linear-gradient(135deg,#9fc5dc,#e6d2a7)}
.t2{background:linear-gradient(135deg,#b7a497,#e8e1d6)}
.t3{background:linear-gradient(135deg,#a8c6d8,#d9cdb9)}
.t4{background:linear-gradient(135deg,#c8d6b4,#e9e2cf)}
.post-text{position:absolute;left:740px;top:44px;width:300px}
.post-text .date{font-size:10px;color:var(--muted)}
.post-text h5{margin-top:6px;font-size:13px;font-weight:700;color:var(--ink)}
.post-text p{margin-top:6px;font-size:11px;line-height:1.6;color:var(--muted)}
.post-text .read{margin-top:6px;display:inline-block;font-size:11px;font-weight:700;color:var(--purple)}
.pager{margin-top:16px;display:flex;gap:6px;justify-content:center;width:696px}
.pager span{width:8px;height:8px;border-radius:50%;background:var(--line)}
.pager span.on{background:var(--purple)}

/* testimonials */
.testimonials{position:absolute;top:1548px;left:0;width:1200px;height:212px;background:linear-gradient(180deg,var(--gold) 0%,var(--gold-deep) 100%)}
.testimonials h2{text-align:center;margin-top:16px;font-size:16px;font-weight:800;color:var(--white);text-transform:uppercase;letter-spacing:1px}
.client-photo{position:absolute;left:80px;top:60px;width:110px;height:110px;border-radius:50%;background:linear-gradient(135deg,#e8d2bd,#b48a6a);border:4px solid var(--white)}
.quote{position:absolute;left:226px;top:66px;width:880px;font-size:13px;font-style:italic;line-height:1.7;color:#5a4410}
.author{position:absolute;left:226px;top:150px;font-size:12px;font-weight:700;color:#5a4410}
.testimonials .arrow.prev{left:18px;top:90px}
.testimonials .arrow.next{right:18px;top:90px}

/* steps */
.steps{top:1832px;height:216px;display:grid;grid-template-columns:repeat(4,1fr)}
.step-intro{background:var(--purple);color:var(--white);padding:24px 22px}
.step-intro h3{font-size:22px;font-weight:400;line-height:1.2}
.step-intro h3 b{font-weight:800;font-size:26px}
.step-intro p{margin-top:10px;font-size:11px;line-height:1.6;color:#e3d3ea}
.btn-outline{display:inline-block;margin-top:12px;border:1px solid var(--white);font-size:10px;font-weight:700;padding:4px 12px}
.step{color:var(--white);text-align:center;padding-top:36px}
.step.s1{background:#4b4b4b}.step.s2{background:#3f3f3f}.step.s3{background:#343434}
.step svg{width:46px;height:46px}
.step h4{margin-top:14px;font-size:19px;font-weight:800}
.step p{margin:8px auto 0;width:200px;font-size:11px;line-height:1.6;color:#bdbdbd}

/* affiliates */
.affiliates{top:2076px;display:flex;align-items:center;gap:22px}
.affiliates h3{width:150px;font-size:15px;font-weight:800;color:var(--purple);text-transform:uppercase}
.aff{width:150px;height:60px;border:1px solid var(--line);display:flex;align-items:center;justify-content:center}
.aff span{display:block;width:90px;height:18px;border-radius:9px;background:#d6d6d6}

/* footer */
.site-footer{position:absolute;top:2208px;left:0;width:1200px;height:252px;background:var(--footer)}
.footer-cols{top:28px;display:grid;grid-template-columns:repeat(4,1fr);gap:30px}
.footer-cols h6{font-size:12px;font-weight:800;color:var(--white);text-transform:uppercase}
.footer-cols p,.footer-cols li{font-size:11px;line-height:1.75;color:#a9a9a9;list-style:none}
.footer-cols p{margin-top:12px}
.footer-cols ul{margin-top:12px}
.map-link{margin-top:6px;display:flex;align-items:center;gap:6px;font-size:11px;color:var(--white)}
.map-link i{width:10px;height:10px;border-radius:50%;background:var(--gold);display:block}
.footer-bottom{position:absolute;top:2460px;left:0;width:1200px;height:88px;background:var(--footer-bottom)}
.footer-brand{position:absolute;left:80px;top:30px;font-size:24px;font-weight:800;color:#8a8a8a}
.copyright{position:absolute;left:300px;top:32px;font-size:10px;line-height:1.6;color:#8a8a8a}
.social{position:absolute;right:80px;top:32px;display:flex;gap:8px}
.social span{width:24px;height:24px;border-radius:50%;background:#4a4a4a}
</style>
</head>
<body>

<header class="site-header">
  <div class="brand"><span class="brand-dot"></span>PlumHarborFit</div>
  <div class="tagline">START LOSING WEIGHT TODAY.... 555 902 6148</div>
  <div class="utility"><a href="#">SUPPORT</a><a href="#">LOGIN</a></div>
  <nav class="main-nav">
    <a class="current" href="#">Home</a>
    <a href="#">Who we are</a>
    <a href="#">What we do</a>
    <a href="#">Who we serve</a>
    <a href="#">Contact</a>
    <a href="#">Blog</a>
    <a href="#">Members</a>
    <svg class="search" viewBox="0 0 16 16"><circle cx="7" cy="7" r="5" fill="none" stroke="#555" stroke-width="2"/><line x1="10.5" y1="10.5" x2="15" y2="15" stroke="#555" stroke-width="2"/></svg>
  </nav>
</header>

<section class="hero">
  <div class="hero-art" role="img" aria-label="Illustrated gym scene in soft blue with a smiling woman holding a dumbbell and an apple"></div>
  <div class="hero-figure"></div>
  <h1 class="hero-title">Vital keys to a healthy heart</h1>
  <div class="hero-sub">Lorem ipsum et dolor</div>
  <div class="hero-note">14 days to a happier, healthier you</div>
  <svg class="arrow prev" viewBox="0 0 34 34"><polyline points="22,6 10,17 22,28" fill="none" stroke="#ffffff" stroke-width="4"/></svg>
  <svg class="arrow next" viewBox="0 0 34 34"><polyline points="12,6 24,17 12,28" fill="none" stroke="#ffffff" stroke-width="4"/></svg>
</section>

<section class="member-band">
  <p>Not a member yet? Sign up today!</p>
  <a class="btn-gold" href="#">Register now</a>
</section>

<section class="wrap features">
  <article class="feature">
    <div class="feature-photo photo-workout" role="img" aria-label="Photo of a woman training with weights"><span class="tag">Read more</span></div>
    <h3>Workout</h3>
    <p>Donec id elit non mi porta gravida at eget metus. Fusce dapibus, tellus ac cursus commodo, tortor mauris condimentum nibh, ut fermentum massa justo sit amet risus. Etiam porta sem malesuada magna mollis.</p>
  </article>
  <article class="feature">
    <div class="feature-photo photo-living" role="img" aria-label="Photo of a woman stretching outdoors"><span class="tag">Read more</span></div>
    <h3>Healthy living</h3>
    <p>Donec id elit non mi porta gravida at eget metus. Fusce dapibus, tellus ac cursus commodo, tortor mauris condimentum nibh, ut fermentum massa justo sit amet risus. Etiam porta sem malesuada magna mollis.</p>
  </article>
  <article class="feature">
    <div class="feature-photo photo-loss" role="img" aria-label="Photo of a woman measuring her waist"><span class="tag">Read more</span></div>
    <h3>Weight loss</h3>
    <p>Donec id elit non mi porta gravida at eget metus. Fusce dapibus, tellus ac cursus commodo, tortor mauris condimentum nibh, ut fermentum massa justo sit amet risus. Etiam porta sem malesuada magna mollis.</p>
  </article>
</section>

<div class="benefits-band"></div>
<section class="wrap benefits">
  <div class="benefit">
    <div class="benefit-head">
      <span class="benefit-icon"><svg width="24" height="24" viewBox="0 0 24 24"><path d="M12 21 3 12a5 5 0 0 1 9-6 5 5 0 0 1 9 6z" fill="#fff"/></svg></span>
      <h4>Heart health</h4>
    </div>
    <ul><li>Cardio sessions for every fitness level</li><li>Lower blood pressure naturally</li><li>Heart friendly meal planning</li><li>Weekly progress check ins</li></ul>
  </div>
  <div class="benefit">
    <div class="benefit-head">
      <span class="benefit-icon"><svg width="26" height="26" viewBox="0 0 26 26"><rect x="2" y="8" width="4" height="10" fill="#fff"/><rect x="20" y="8" width="4" height="10" fill="#fff"/><rect x="6" y="11" width="14" height="4" fill="#fff"/></svg></span>
      <h4>Muscle gain</h4>
    </div>
    <ul><li>Strength plans built around you</li><li>Protein rich recipes and tips</li><li>Proper form and safe lifting</li><li>Recovery and rest guidance</li></ul>
  </div>
  <div class="benefit">
    <div class="benefit-head">
      <span class="benefit-icon"><svg width="24" height="24" viewBox="0 0 24 24"><rect x="3" y="5" width="18" height="15" rx="3" fill="none" stroke="#fff" stroke-width="2"/><line x1="12" y1="9" x2="15" y2="13" stroke="#fff" stroke-width="2"/></svg></span>
      <h4>Slimming</h4>
    </div>
    <ul><li>Sustainable weight loss habits</li><li>Simple portion control methods</li><li>Fat burning interval training</li><li>Mindful eating coaching</li></ul>
  </div>
</section>

<section class="wrap callout">
  <p>Utmsi enim ad minim veniam, quis nostrud exerci tation ullamcorper suscipit lobor tis nisl ut aliquip ex ea commodo consequat.</p>
  <a class="more-circle" href="#">FIND OUT<br>MORE</a>
  <span class="pill">VIEW ALL</span>
</section>

<section class="wrap latest">
  <h2 class="section-title">Latest posts</h2>
  <div class="post-grid">
    <div class="post-thumb t1" role="img" aria-label="Photo of friends jogging on a beach"></div>
    <div class="post-thumb t2" role="img" aria-label="Photo of a woman lifting weights"></div>
    <div class="post-thumb t3" role="img" aria-label="Photo of a group exercising outdoors"></div>
    <div class="post-thumb t4" role="img" aria-label="Photo of a woman meditating on grass"></div>
  </div>
  <div class="pager"><span class="on"></span><span></span><span></span></div>
  <div class="post-text">
    <div class="date">17 November 2014 | Admin</div>
    <h5>Why you should meditate</h5>
    <p>Donec id elit non mi porta gravida at eget metus. Fusce dapibus, tellus ac cursus commodo, tortor mauris condimentum nibh, ut fermentum massa justo sit amet risus.</p>
    <a class="read" href="#">Read more</a>
  </div>
</section>

<section class="testimonials">
  <h2>Testimonials</h2>
  <div class="client-photo" role="img" aria-label="Portrait photo of a client"></div>
  <p class="quote">“Sed ut perspiciatis unde omnis iste natus error sit voluptatem accusantium doloremque laudantium, totam rem aperiam, eaque ipsa quae ab illo inventore veritatis et quasi architecto beatae vitae dicta sunt explicabo. Nemo enim ipsam voluptatem quia voluptas sit aspernatur aut odit aut fugit.”</p>
  <div class="author">— Dana Whitlow, Nutritionist</div>
  <svg class="arrow prev" viewBox="0 0 34 34"><polyline points="22,6 10,17 22,28" fill="none" stroke="#ffffff" stroke-width="4"/></svg>
  <svg class="arrow next" viewBox="0 0 34 34"><polyline points="12,6 24,17 12,28" fill="none" stroke="#ffffff" stroke-width="4"/></svg>
</section>

<section class="wrap steps">
  <div class="step-intro">
    <h3>Improve your lifestyle<br>in <b>3 steps</b></h3>
    <p>Donec id elit non mi porta gravida at eget metus. Fusce dapibus, tellus ac cursus commodo tortor.</p>
    <a class="btn-outline" href="#">Read more</a>
  </div>
  <div class="step s1">
    <svg viewBox="0 0 46 46"><circle cx="23" cy="26" r="15" fill="none" stroke="#fff" stroke-width="3"/><line x1="23" y1="26" x2="23" y2="17" stroke="#fff" stroke-width="3"/><rect x="19" y="4" width="8" height="4" fill="#fff"/></svg>
    <h4>Lorem Ipsum</h4>
    <p>Donec id elit non mi porta gravida at eget metus fusce dapibus.</p>
  </div>
  <div class="step s2">
    <svg viewBox="0 0 46 46"><path d="M23 14c-8-6-17 0-15 12 2 10 10 16 15 12 5 4 13-2 15-12 2-12-7-18-15-12z" fill="none" stroke="#fff" stroke-width="3"/><line x1="23" y1="14" x2="26" y2="5" stroke="#fff" stroke-width="3"/></svg>
    <h4>Dui Autem Vel</h4>
    <p>Donec id elit non mi porta gravida at eget metus fusce dapibus.</p>
  </div>
  <div class="step s3">
    <svg viewBox="0 0 46 46"><rect x="4" y="15" width="6" height="16" fill="#fff"/><rect x="36" y="15" width="6" height="16" fill="#fff"/><rect x="10" y="21" width="26" height="4" fill="#fff"/></svg>
    <h4>Nam Limber</h4>
    <p>Donec id elit non mi porta gravida at eget metus fusce dapibus.</p>
  </div>
</section>

<section class="wrap affiliates">
  <h3>Our affiliates</h3>
  <div class="aff"><span></span></div>
  <div class="aff"><span></span></div>
  <div class="aff"><span></span></div>
  <div class="aff"><span></span></div>
  <div class="aff"><span></span></div>
</section>

<footer class="site-footer">
  <div class="wrap footer-cols">
    <div>
      <h6>PlumHarborFit</h6>
      <p>Personal coaching for busy professionals who value health, energy and time. Train smarter, eat better and feel your best every day with a plan made for you.</p>
    </div>
    <div>
      <h6>Important links</h6>
      <ul><li>Register</li><li>Blog</li><li>Disclaimer</li><li>Privacy Policy</li><li>Terms and Conditions</li></ul>
    </div>
    <div>
      <h6>Verse of the day</h6>
      <p>Those who hope renew their strength. They will soar on wings like eagles; they will run and not grow weary, they will walk and not be faint.</p>
    </div>
    <div>
      <h6>Get in touch</h6>
      <ul><li>T: (555) 902-6148</li><li>Email: hello@plumharborfit.com</li><li>PlumHarborFit Studio</li><li>214 Harbor St, Plumfield</li></ul>
      <div class="map-link"><i></i>Open in Map</div>
    </div>
  </div>
</footer>
<div class="footer-bottom">
  <div class="footer-brand">PlumHarborFit</div>
  <div class="copyright">Copyright © 2014 PlumHarborFit. All Rights Reserved.<br>Disclaimer | Privacy Policy</div>
  <div class="social"><span></span><span></span><span></span></div>
</div>

</body>
</html>
```